New Business Card for General Contractor Marketing

Need a business card the is more like a marketing promotion of our services
Must be horizontal orientation, One Sided Only, Max font size, Organize the Services
#1 General Contractor for Realtors
Remodels – Renovations – Repairs
Water & Mold Damage Experts
Painting: Interior/ Exterior
Flooring: Wood / LVT / Carpet
Plumbing: Repairs & Upgrades
Electric: Lights & Energy Efficient Upgrades
Kitchen & Bath Remodels
Fast Inspections Repair Billed Thru Escrow
BrightHarborBuilds.com
555-418-2796

Industry/Entity Type

General Contractor

Contact Information for Business Card

One Sided Only: #1 General Contractor for Realtors Remodels – Renovations – Repairs Water & Mold Damage Experts Painting: Interior/ Exterior Flooring: Wood / LVT / Carpet Plumbing: Repairs & Upgrades Electric: Lights & Energy Efficient Upgrades Kitchen & Bath Remodels Fast Inspections Repair Billed Thru Escrow BrightHarborBuilds.com 555-418-2796

Colors
0054AA
0677BA
7BADD7
CADEEF
E8F1F8

Requirements
Must have
• One Sided Only: #1 General Contractor for Realtors Remodels – Renovations – Repairs Water & Mold Damage Experts Painting: Interior/ Exterior Flooring: Wood / LVT / Carpet Plumbing: Repairs & Upgrades Electric: Lights & Energy Efficient Upgrades Kitchen & Bath Remodels Fast Inspections Repair Billed Thru Escrow BrightHarborBuilds.com 555-418-2796

```html
<!DOCTYPE html>
<html lang="en">
<head>
<meta charset="UTF-8">
<title>Harbor Crest Remodel – Business Card</title>
<link href="https://fonts.googleapis.com/css2?family=Bebas+Neue&family=Montserrat:wght@500;800&display=swap" rel="stylesheet">
<style>
  :root {
    --navy: #17295c;
    --blue: #0054aa;
    --sky: #7badd7;
    --mist: #cadeef;
    --white: #ffffff;
    --backdrop: #3b3b3d;
  }
  * { box-sizing: border-box; margin: 0; padding: 0; }
  html, body { width: 1200px; height: 1200px; overflow: hidden; }
  body {
    background: var(--backdrop);
    display: flex; align-items: center; justify-content: center;
    font-family: "Montserrat", sans-serif;
  }
  .card {
    position: relative;
    width: 1140px; height: 651px;
    border-radius: 44px;
    overflow: hidden;
    background: var(--white);
    box-shadow: 0 20px 50px rgba(0,0,0,.45);
  }
  .card__top {
    height: 278px;
    display: flex; flex-direction: column; align-items: center; justify-content: center;
    gap: 34px;
    padding: 14px 48px 0;
  }
  .brand { display: flex; align-items: center; gap: 20px; }
  .brand__dot { width: 46px; height: 46px; border-radius: 50%; background: var(--blue); }
  .brand__name {
    font-weight: 800; font-size: 60px; color: var(--navy);
    letter-spacing: 1px; text-transform: uppercase; white-space: nowrap;
  }
  .headline {
    font-weight: 800; font-size: 42px; color: var(--navy);
    text-transform: uppercase; letter-spacing: 1px; white-space: nowrap;
  }
  .headline__rank { font-size: 56px; }
  .card__band { height: 36px; background: var(--sky); }
  .card__body {
    height: 337px; background: var(--navy);
    display: flex; flex-direction: column; align-items: center;
    padding: 24px 56px 0;
    font-family: "Bebas Neue", sans-serif;
    color: var(--white);
  }
  .services { text-align: center; }
  .services__line { font-size: 32px; line-height: 42px; white-space: nowrap; letter-spacing: .3px; }
  .services__label { color: var(--sky); }
  .escrow { margin-top: 18px; font-size: 38px; color: var(--sky); letter-spacing: .5px; white-space: nowrap; }
  .contact {
    margin-top: 20px;
    display: flex; align-items: center; gap: 56px;
    font-family: "Montserrat", sans-serif; font-weight: 500; font-size: 38px;
    white-space: nowrap;
  }
  .contact__item { display: flex; align-items: center; gap: 14px; }
  .contact__icon { width: 42px; height: 42px; }
</style>
</head>
<body>
  <div class="card">
    <header class="card__top">
      <div class="brand">
        <span class="brand__dot"></span>
        <span class="brand__name">Harbor Crest Remodel</span>
      </div>
      <h1 class="headline"><span class="headline__rank">#1</span> General Contractor for Realtors</h1>
    </header>
    <div class="card__band"></div>
    <section class="card__body">
      <div class="services">
        <p class="services__line">Realtors Remodels • Renovations • Repairs Water &amp; Mold Damage</p>
        <p class="services__line"><span class="services__label">Painting:</span> Interior/ Exterior • <span class="services__label">Flooring:</span> Wood / LVT / Carpet • <span class="services__label">Plumbing:</span> Repairs &amp; Upgrades</p>
        <p class="services__line"><span class="services__label">Electric:</span> Lights &amp; Energy Efficient Upgrades • Kitchen &amp; Bath Remodels</p>
      </div>
      <p class="escrow">Fast Inspections Repair Billed Thru Escrow</p>
      <div class="contact">
        <div class="contact__item">
          <svg class="contact__icon" viewBox="0 0 24 24" aria-hidden="true"><path fill="#7badd7" d="M6.6 10.8a15.1 15.1 0 0 0 6.6 6.6l2.2-2.2a1 1 0 0 1 1-.25 11.4 11.4 0 0 0 3.6.57 1 1 0 0 1 1 1V20a1 1 0 0 1-1 1A17 17 0 0 1 3 4a1 1 0 0 1 1-1h3.5a1 1 0 0 1 1 1c0 1.25.2 2.45.57 3.6a1 1 0 0 1-.25 1z"/></svg>
          <span>555-418-2796</span>
        </div>
        <div class="contact__item">
          <svg class="contact__icon" viewBox="0 0 24 24" aria-hidden="true" fill="none" stroke="#7badd7" stroke-width="1.8"><circle cx="12" cy="12" r="9.5"/><ellipse cx="12" cy="12" rx="4.2" ry="9.5"/><path d="M2.5 12h19M4 7h16M4 17h16"/></svg>
          <span>BrightHarborBuilds.com</span>
        </div>
      </div>
    </section>
  </div>
</body>
</html>
```